Etiketten-Design für nachhaltige Rasur- & Pflegeprodukte
Mit Rosalind haben wir einen sehr freundlichen Kontakt, auch im Nachhinein waren noch Anpassungen möglich. Außerdem zeigt sie sich verständnisvoll, von unserer Seite hat sich die Lieferung von Infos manchmal verzögert. Sie dagegen ist schnell wie der Blitz. Das Ergebnis ihrer Arbeit ist außerdem herausragend, wir sind begeistert. Liebe Grüße Jens
> Wir suchen Verpackung und Etiketten für eine Marke für nachhaltige Rasur- & Pflegeprodukte.
Habedere liebe Designer,
„Habedere“ sagt man bei uns in Bayern, es bedeutet Hallo oder auf Wiedersehen, je nach Gelegenheit. In diesem Fall: Hallo.
Vielleicht kennst du uns schon, wir sind tidewinders, wir betreiben einen kleinen Shop für Bartpflege & Rasur unter tidewinders.example und wir versuchen uns nun an einem neuen Thema: nachhaltige Rasur- & Pflegeprodukte für Frauen.
Das machen wir unter dem Namen „Flau“.
Weil die Frage schon oft aufkam: Jawohl, wir haben uns dafür die Beine und die Achseln mit einem Rasierhobel rasiert.
> Zielgruppe.
Wir arbeiten an einer neuen Pflegelinie für Frauen, die sich vorwiegend mit der Rasur und den dazugehörigen Pflegeprodukten beschäftigt. Die Zielgruppe sind vor allem online-affine Frauen aus Deutschland, Österreich und der Schweiz, aber sicher auch europaweit im Alter von 21-45.
> Aufgabenstellung.
Wir sind auf der Suche nach einem Konzept für unsere Produktverpackungen bzw. Etiketten. Bei den Pflegeprodukten verzichten wir bewusst auf eine Umverpackung.
Konkret geplant sind ein Rasierhobel, dafür haben wir eine schöne Umverpackung. Außerdem starten wir mit Rasieröl, Rasierseife und einem After Shave Balsam. Es werden später noch andere Artikel dazukommen, eine Deocreme zum Beispiel.
Rasieröl, Rasiercreme und After Shave Balsam duften nach Orangen, es werden zwei oder drei weitere Duftrichtungen folgen, die eine wird beispielsweise nach Beeren duften, die andere nach Pfirsich und Mango – bitte beachte das bei der Erstellung des Konzeptes, die Unterschiede sollten später auf den ersten Blick erkennbar sein.
Zurück zum Thema Orange: Wir würden den Duft als leicht herben Zitrusduft bezeichnen.
> Die Maße.
• Umverpackung Rasierhobel, weißer Karton (165x90x40mm)
• Rasieröl 30ml (Etikett: 100x46mm)
• Rasiercreme 60ml (Etikett: 156x32mm)
• After Shave Balsam 60ml (Etikett: 156x32mm)
> Zwingend erforderliche Angaben.
Da es sich um Kosmetikprodukte handelt, sind einige Angaben auf dem Label zwingend erforderlich, beispielhaft sollen die folgenden Infos als Platzhalter dienen.
• Hergestellt für Torsten Kählbrink e.K. von tidewinders, Holunderweg 27, 83047 Rosenheim
• Ingredients: Aqua, Stearic Acid, Cocos Nucifera oil, Glycerin, Potassium Hydroxide, Litsea Cubeba oil, (and) Citrus Sinensis Peel oil, Orbignya Oleifera oil, Sodium Hydroxide, Macadamia ternifolia oil, Talc, Kaolin, Citric Acid, Simmondsia chinensis oil, Maris sal, C.I. 77892 (and) Rad Clay, Citral, Limonene, Linalool, Geraniol
• Platz für einen Barcode
• Rasieröl sind 30ml / 1.01 FL.OZ. ODER Creme & Balsam jeweils 60ml / 2.03 FL. OZ.
Wir haben ein Bild der aktuellen Gefäße beigefügt, es kann aber durchaus sein, dass wir uns noch umen..

```html
<!DOCTYPE html>
<html lang="de">
<head>
<meta charset="utf-8">
<title>Flau – Umverpackung Rasierhobel</title>
<link rel="stylesheet" href="https://fonts.googleapis.com/css2?family=Comfortaa:wght@400;700&family=Courgette&family=Mulish:wght@400&family=Kaushan+Script&display=swap">
<style>
:root{
  --sheet:#f9f3f3;
  --panel:#ffffff;
  --sage:#8aa89f;
  --pink:#d67fd8;
  --pink-soft:#f1c9f0;
  --mint:#84cdbd;
  --mint-soft:#cfe8e0;
  --ink:#555a58;
  --white:#ffffff;
}
*{box-sizing:border-box;margin:0;padding:0}
html,body{width:903px;height:1200px;overflow:hidden;background:var(--white)}
.canvas{width:903px;height:1200px;display:flex;flex-direction:column;align-items:center;justify-content:center;gap:16px}
.dieline{width:500px;height:376px;background:var(--sheet);display:flex;align-items:center;justify-content:center;gap:12px}
.panel{position:relative;width:148px;height:336px;background:var(--panel);overflow:hidden;display:flex;flex-direction:column;align-items:center}
.feather-field{position:absolute;inset:0;z-index:0}
.theme-pink .feather-field{background:
  radial-gradient(ellipse 22px 10px at 18% 6%,var(--pink-soft),transparent 70%),
  radial-gradient(ellipse 22px 10px at 82% 94%,var(--pink-soft),transparent 70%),
  radial-gradient(ellipse 18px 9px at 88% 40%,var(--pink-soft),transparent 70%),
  radial-gradient(ellipse 18px 9px at 10% 70%,var(--pink-soft),transparent 70%),
  var(--panel)}
.theme-mint .feather-field{background:
  radial-gradient(ellipse 22px 10px at 18% 6%,var(--mint-soft),transparent 70%),
  radial-gradient(ellipse 22px 10px at 82% 94%,var(--mint-soft),transparent 70%),
  radial-gradient(ellipse 18px 9px at 88% 42%,var(--mint-soft),transparent 70%),
  radial-gradient(ellipse 18px 9px at 10% 72%,var(--mint-soft),transparent 70%),
  var(--panel)}
.content{position:relative;z-index:1;width:100%;height:100%;display:flex;flex-direction:column;align-items:center}
.brand-disc{margin-top:52px;width:92px;height:92px;border-radius:50%;background:var(--sage);display:flex;align-items:center;justify-content:center}
.brand-name{font-family:'Comfortaa',sans-serif;font-weight:400;font-size:24px;color:var(--white)}
.front-title{margin-top:28px;text-align:center;line-height:1.15}
.feather-mark{width:58px;height:22px;border-radius:50%;margin-top:16px;background:linear-gradient(90deg,var(--pink-soft),var(--mint-soft))}
.feather-mark.small{width:26px;height:8px;margin:6px 0}
.theme-mint .feather-mark{background:linear-gradient(90deg,var(--mint-soft),var(--mint))}
.script-pink{font-family:'Kaushan Script',cursive;color:var(--pink)}
.script-mint{font-family:'Courgette',cursive;color:var(--mint)}
.round-mint{font-family:'Comfortaa',sans-serif;color:var(--mint)}
.front-title .line1{font-size:18px;display:block}
.front-title .line2{font-size:20px;display:block}
.back-title{margin-top:34px;text-align:center;line-height:1.25}
.back-title .line1{font-size:13px;display:block}
.back-title .line2{font-size:14px;display:block}
.how-to{font-family:'Mulish',sans-serif;font-size:11px;color:var(--ink);margin-top:3px}
.step{font-family:'Comfortaa',sans-serif;font-size:12px;color:var(--mint);margin:6px 0 2px}
.ingredients{font-family:'Mulish',sans-serif;font-size:4.6px;line-height:1.45;color:var(--ink);text-align:justify;width:118px}
.imprint{font-family:'Mulish',sans-serif;font-size:4.4px;line-height:1.4;color:var(--ink);text-align:center;width:100px;margin-top:auto;margin-bottom:18px}
.side{justify-content:center}
.claim{writing-mode:vertical-rl;transform:rotate(180deg);white-space:nowrap}
.claim.down{transform:none}
.claim-script{font-family:'Kaushan Script',cursive;font-size:26px;color:var(--pink)}
.claim-round{font-family:'Comfortaa',sans-serif;font-size:24px;color:var(--mint)}
.claim-pair{font-family:'Mulish',sans-serif;font-size:15px;color:var(--sage);line-height:1.2;text-align:center}
</style>
</head>
<body>
<main class="canvas">

  <!-- Variant A: pink script -->
  <section class="dieline theme-pink">
    <article class="panel front">
      <div class="feather-field" role="img" aria-label="Streumuster aus zarten rosa Federzeichnungen"></div>
      <div class="content">
        <div class="brand-disc"><span class="brand-name">Flau</span></div>
        <h2 class="front-title script-pink"><span class="line1">Beim</span><span class="line2">Rasierhobel</span></h2>
        <div class="feather-mark" role="img" aria-label="Aquarell-Feder in Rosa und Mint"></div>
      </div>
    </article>
    <article class="panel back">
      <div class="feather-field" role="img" aria-label="Streumuster aus zarten rosa Federzeichnungen"></div>
      <div class="content">
        <h3 class="back-title script-pink"><span class="line1">Beim</span><span class="line2">Rasierhobel</span></h3>
        <p class="how-to">How to use:</p>
        <div class="feather-mark small" role="img" aria-label="kleine Feder"></div>
        <p class="ingredients">Aqua, Stearic Acid, Cocos Nucifera oil, Glycerin, Potassium Hydroxide, Litsea Cubeba oil, (and) Citrus Sinensis Peel oil, Orbignya Oleifera oil, Sodium Hydroxide, Macadamia ternifolia oil, Talc, Kaolin, Citric Acid, Simmondsia chinensis oil, Maris sal, C.I. 77892 (and) Rad Clay, Citral,</p>
        <div class="feather-mark small" role="img" aria-label="kleine Feder"></div>
        <p class="ingredients">Aqua, Stearic Acid, Cocos Nucifera oil, Glycerin, Potassium Hydroxide, Litsea Cubeba oil, (and) Citrus Sinensis Peel oil, Orbignya Oleifera oil, Sodium Hydroxide, Macadamia ternifolia oil, Talc, Kaolin, Citric Acid, Simmondsia chinensis oil, Maris sal, C.I. 77892 (and) Rad Clay, Citral,</p>
        <div class="feather-mark small" role="img" aria-label="kleine Feder"></div>
        <p class="ingredients">Aqua, Stearic Acid, Cocos Nucifera oil, Glycerin, Potassium Hydroxide, Litsea Cubeba oil, (and) Citrus Sinensis Peel oil, Orbignya Oleifera oil,</p>
        <p class="imprint">Hergestellt für Torsten Kählbrink e. K. von tidewinders, Holunderweg 27, 83047 Rosenheim.</p>
      </div>
    </article>
    <article class="panel side">
      <div class="feather-field" role="img" aria-label="Streumuster aus zarten rosa Federzeichnungen"></div>
      <div class="content side"><p class="claim claim-script">only for women</p></div>
    </article>
  </section>

  <!-- Variant B: mint with steps -->
  <section class="dieline theme-mint">
    <article class="panel front">
      <div class="feather-field" role="img" aria-label="Streumuster aus mintfarbenen Federzeichnungen"></div>
      <div class="content">
        <div class="brand-disc"><span class="brand-name">Flau</span></div>
        <h2 class="front-title script-mint"><span class="line1">Beim</span><span class="line2">Rasierhobel</span></h2>
        <div class="feather-mark" role="img" aria-label="mintfarbene Feder"></div>
      </div>
    </article>
    <article class="panel back">
      <div class="feather-field" role="img" aria-label="Streumuster aus mintfarbenen Federzeichnungen"></div>
      <div class="content">
        <h3 class="back-title script-mint"><span class="line1">Beim</span><span class="line2">Rasierhobel</span></h3>
        <p class="how-to">How to use:</p>
        <p class="step">STEP 1</p>
        <p class="ingredients">Aqua, Stearic Acid, Cocos Nucifera oil, Glycerin, Potassium Hydroxide, Litsea Cubeba oil, (and) Citrus Sinensis Peel oil, Orbignya Oleifera oil, Sodium Hydroxide, Macadamia ternifolia oil, Talc, Kaolin, Citric Acid, Simmondsia chinensis oil, Maris sal, C.I. 77892 (and) Rad Clay, Citral,</p>
        <p class="step">STEP 2</p>
        <p class="ingredients">Aqua, Stearic Acid, Cocos Nucifera oil, Glycerin, Potassium Hydroxide, Litsea Cubeba oil, (and) Citrus Sinensis Peel oil, Orbignya Oleifera oil, Sodium Hydroxide, Macadamia ternifolia oil, Talc, Kaolin, Citric Acid, Simmondsia chinensis oil, Maris sal, C.I. 77892 (and) Rad Clay, Citral,</p>
        <p class="step">STEP 3</p>
        <p class="ingredients">Aqua, Stearic Acid, Cocos Nucifera oil, Glycerin, Potassium Hydroxide, Litsea Cubeba oil, (and) Citrus Sinensis Peel oil, Orbignya Oleifera oil,</p>
        <div class="feather-mark small" role="img" aria-label="kleine Feder"></div>
        <p class="imprint">Hergestellt für Torsten Kählbrink e. K. von tidewinders, Holunderweg 27, 83047 Rosenheim.</p>
      </div>
    </article>
    <article class="panel side">
      <div class="feather-field" role="img" aria-label="Streumuster aus mintfarbenen Federzeichnungen"></div>
      <div class="content side"><p class="claim down claim-pair">Made with care<br>especially for women</p></div>
    </article>
  </section>

  <!-- Variant C: rounded sans, pink feathers -->
  <section class="dieline theme-pink">
    <article class="panel front">
      <div class="feather-field" role="img" aria-label="Streumuster aus rosa Federn"></div>
      <div class="content">
        <div class="brand-disc"><span class="brand-name">Flau</span></div>
        <h2 class="front-title round-mint"><span class="line1">Beim</span><span class="line2">Rasierhobel</span></h2>
        <div class="feather-mark" role="img" aria-label="Aquarell-Feder in Rosa und Mint"></div>
      </div>
    </article>
    <article class="panel back">
      <div class="feather-field" role="img" aria-label="Streumuster aus rosa Federn"></div>
      <div class="content">
        <h3 class="back-title round-mint"><span class="line1">Beim</span><span class="line2">Rasierhobel</span></h3>
        <p class="how-to">How to use:</p>
        <div class="feather-mark small" role="img" aria-label="kleine Feder"></div>
        <p class="ingredients">Aqua, Stearic Acid, Cocos Nucifera oil, Glycerin, Potassium Hydroxide, Litsea Cubeba oil, (and) Citrus Sinensis Peel oil, Orbignya Oleifera oil, Sodium Hydroxide, Macadamia ternifolia oil, Talc, Kaolin, Citric Acid, Simmondsia chinensis oil, Maris sal, C.I. 77892 (and) Rad Clay, Citral,</p>
        <div class="feather-mark small" role="img" aria-label="kleine Feder"></div>
        <p class="ingredients">Aqua, Stearic Acid, Cocos Nucifera oil, Glycerin, Potassium Hydroxide, Litsea Cubeba oil, (and) Citrus Sinensis Peel oil, Orbignya Oleifera oil, Sodium Hydroxide, Macadamia ternifolia oil, Talc, Kaolin, Citric Acid, Simmondsia chinensis oil, Maris sal, C.I. 77892 (and) Rad Clay, Citral,</p>
        <div class="feather-mark small" role="img" aria-label="kleine Feder"></div>
        <p class="ingredients">Aqua, Stearic Acid, Cocos Nucifera oil, Glycerin, Potassium Hydroxide, Litsea Cubeba oil, (and) Citrus Sinensis Peel oil, Orbignya Oleifera oil,</p>
        <p class="imprint">Hergestellt für Torsten Kählbrink e. K. von tidewinders, Holunderweg 27, 83047 Rosenheim.</p>
      </div>
    </article>
    <article class="panel side">
      <div class="feather-field" role="img" aria-label="Streumuster aus rosa Federn"></div>
      <div class="content side"><p class="claim claim-round">only for women</p></div>
    </article>
  </section>

</main>
</body>
</html>
```